Home Page Design

Please see design brief attached. Concept here: sketchboard[dot]io/file/qWm83LzpR7cvXuNtYa2KhE/Brindlemoor---Landing-Page?node-id=0%3A1&t=PKr92mvnQsD4xTcZ-1

Industry/Entity Type

Wedding

Number of Pages Required

1 page

Font styles to use
Serif
Sans Serif
Decorative
Script

Colors
A7469A
B969AE
D3A5CF
EDDBEB
F8F0F9
6B429C
8869AF
B7A5CE
E3DAEB
F3F0F8

Requirements
Must have
• Please see attached PDF
Nice to have
• Please see attached PDF
Should not have
• Please see attached PDF

```html
<!DOCTYPE html>
<html lang="en">
<head>
<meta charset="utf-8">
<title>Brindlemoor – Wedding Vendors</title>
<link href="https://fonts.googleapis.com/css2?family=Playfair+Display:ital,wght@0,400;0,500;0,600;1,400&family=Poppins:wght@400;500;600&display=swap" rel="stylesheet">
<style>
:root{
  --purple:#6a2c7b;
  --purple-dark:#55205f;
  --purple-mid:#8a3d98;
  --lilac:#b969ae;
  --lilac-soft:#d3a5cf;
  --blush:#f8f0f9;
  --blush-2:#fbf4fb;
  --ink:#222;
  --muted:#555;
  --white:#fff;
  --gold:#f2b21b;
}
*{margin:0;padding:0;box-sizing:border-box}
html,body{width:1200px;height:4743px;overflow:hidden;background:#fff}
body{font-family:'Poppins',sans-serif;color:var(--ink)}
.page{position:relative;width:1200px;height:4743px;overflow:hidden}
.abs{position:absolute}
.serif{font-family:'Playfair Display',serif}
.photo{position:absolute}

/* header */
.header{position:absolute;left:0;top:0;width:1200px;height:88px;background:#fff;border-top:3px solid var(--purple)}
.logo{position:absolute;left:100px;top:22px;display:flex;align-items:center;gap:10px}
.logo-dot{width:14px;height:14px;border-radius:50%;background:var(--purple)}
.logo-name{font-family:'Playfair Display',serif;font-size:28px;color:var(--purple);font-weight:400}
.logo-tag{position:absolute;left:124px;top:74px;font-size:6px;letter-spacing:1px;color:#999;text-transform:uppercase}
.nav{position:absolute;top:36px;font-size:15px;color:#222}
.btn-vendor{position:absolute;left:900px;top:24px;width:200px;height:40px;border-radius:20px;background:var(--purple);color:#fff;font-size:15px;display:flex;align-items:center;justify-content:center}

/* hero */
.hero{top:88px;left:0;width:1200px;height:628px;background:radial-gradient(ellipse at 50% 30%,#8a8a70 0%,#4e5a3e 45%,#2b2f24 100%)}
.hero-shade{position:absolute;left:0;top:88px;width:1200px;height:628px;background:linear-gradient(180deg,rgba(0,0,0,.05),rgba(0,0,0,.35))}
.hero-title{position:absolute;left:0;top:440px;width:1200px;text-align:center;color:#fff;font-family:'Playfair Display',serif;font-size:37px}
.hero-sub{position:absolute;left:280px;top:498px;width:640px;text-align:center;color:#fff;font-size:16px;line-height:28px}
.search{position:absolute;left:325px;top:573px;width:545px;height:40px;display:flex}
.search-field{background:#fff;height:40px;display:flex;align-items:center;justify-content:space-between;padding:0 16px;font-size:14px;color:#333}
.search-btn{background:var(--purple);color:#fff;width:120px;font-size:15px;display:flex;align-items:center;justify-content:center}

/* features */
.features{top:716px;left:0;width:1200px;height:730px;background:var(--blush-2)}
.section-title{position:absolute;left:0;width:1200px;text-align:center;font-family:'Playfair Display',serif;font-size:37px;color:#111}
.feature{position:absolute;width:236px;height:188px;background:#fff;box-shadow:0 2px 6px rgba(0,0,0,.08);text-align:center}
.feature .ic{margin:18px auto 0;width:74px;height:74px;border-radius:50%;border:2px solid var(--purple);display:flex;align-items:center;justify-content:center}
.feature p{font-size:12px;line-height:20px;color:#222;padding:14px 10px 0}
.btn{position:absolute;background:var(--purple);color:#fff;border-radius:20px;display:flex;align-items:center;justify-content:center;font-size:14px;font-weight:500;letter-spacing:.5px}

/* vendors */
.vendor{position:absolute;width:242px;height:236px;border-radius:6px;overflow:hidden}
.vendor span{position:absolute;left:12px;bottom:10px;color:#fff;font-family:'Playfair Display',serif;font-size:16px;border-left:2px solid var(--lilac);padding-left:6px}
.vendor i{position:absolute;left:0;bottom:0;width:100%;height:60px;background:linear-gradient(0deg,rgba(0,0,0,.6),rgba(0,0,0,0))}

/* how */
.how{top:2172px;left:0;width:1200px;height:432px;background:linear-gradient(180deg,#5c2569,#7a3689 60%,#6a2c7b)}
.step{position:absolute;width:192px;height:192px;top:2337px;border-radius:50%;background:#fff;text-align:center;box-shadow:0 0 0 6px rgba(255,255,255,.35)}
.step svg.ring{position:absolute;left:-8px;top:-8px}
.step .ic{margin:34px auto 0;width:60px;height:60px}
.step p{font-family:'Playfair Display',serif;font-size:14px;line-height:20px;font-weight:600;color:#333;padding:2px 12px 0}
.arrow{position:absolute;top:2425px}

/* about */
.about{top:2604px;left:0;width:1200px;height:533px;background:linear-gradient(90deg,#e8d6c2 0%,#f3e6d6 40%,#cdb8a3 70%,#8f7766 100%)}
.about-box{position:absolute;left:104px;top:2697px;width:424px;height:348px;background:#fff;box-shadow:0 4px 14px rgba(0,0,0,.12)}
.about-box:before{content:"";position:absolute;left:6px;top:6px;right:6px;bottom:6px;border:2px solid var(--purple)}
.about-box h2{position:absolute;left:24px;top:18px;font-family:'Playfair Display',serif;font-size:36px;font-weight:400}
.about-box p{position:absolute;left:24px;top:74px;width:376px;font-size:15px;line-height:29px;color:#555;text-align:justify}

/* clients */
.clients{top:3137px;left:0;width:1200px;height:433px;background:var(--blush-2)}
.underline{position:absolute;width:84px;height:2px;background:#222;left:558px}
.underline b{position:absolute;left:27px;top:-1px;width:30px;height:4px;background:var(--purple)}
.quote{position:absolute;left:200px;top:3296px;width:800px;text-align:center;font-family:'Playfair Display',serif;font-style:italic;font-size:15px;line-height:31px;color:#444}

/* blog */
.post{position:absolute;top:3764px;width:313px;height:419px;background:#fff;box-shadow:0 2px 8px rgba(0,0,0,.1)}
.post .img{height:210px}
.post h3{font-family:'Playfair Display',serif;font-weight:400;font-size:21px;line-height:26px;padding:18px 16px 0;color:#222}
.post p{font-size:12px;line-height:27px;color:#333;padding:8px 16px 0}
.post a{display:inline-block;margin:4px 0 0 20px;font-size:14px;color:var(--purple);text-decoration:underline;font-weight:500}

/* footer */
.footer{top:4345px;left:0;width:1200px;height:398px;background:var(--purple)}
.signup{position:absolute;left:140px;top:4288px;width:920px;height:104px;background:#fff;border-radius:52px;border:1px solid #eee}
.signup h4{position:absolute;left:40px;top:26px;font-family:'Playfair Display',serif;font-weight:400;font-size:25px;line-height:32px;color:#222}
.signup .inputs{position:absolute;left:328px;top:30px;width:404px;height:44px;border:1px solid #ddd;border-radius:22px 0 0 22px;display:flex;align-items:center;font-size:14px;color:#444}
.signup .submit{position:absolute;left:732px;top:30px;width:145px;height:44px;background:var(--purple);border-radius:0 22px 22px 0;color:#fff;font-size:16px;font-weight:600;display:flex;align-items:center;justify-content:center}
.fcol{position:absolute;top:4450px;color:#fff}
.fcol h5{font-family:'Playfair Display',serif;font-weight:400;font-size:20px;color:#eedcef;margin-bottom:10px}
.fcol li{list-style:none;font-size:14px;line-height:31px}
.social{position:absolute;top:4587px;width:34px;height:34px;border:1.5px solid #fff;border-radius:50%}
.copy{position:absolute;left:0;top:4703px;width:1200px;text-align:center;font-size:14px;color:#fff}
.fline{position:absolute;left:0;top:4685px;width:1200px;height:1px;background:rgba(255,255,255,.25)}
</style>
</head>
<body>
<div class="page">

<header class="header">
  <div class="logo"><span class="logo-dot"></span><span class="logo-name">Brindlemoor</span></div>
  <div class="logo-tag">Weddings, events &amp; planning</div>
  <span class="nav" style="left:330px">Home</span>
  <span class="nav" style="left:413px">Vendors</span>
  <span class="nav" style="left:515px">Blog</span>
  <span class="nav" style="left:586px">Contact Us</span>
  <span class="nav" style="left:710px">Wedding Calculator</span>
  <div class="btn-vendor">sign up as a vendor</div>
</header>

<section>
  <div class="photo hero" role="img" aria-label="Photo of a bride and groom kissing outdoors while guests throw petals"></div>
  <div class="hero-shade"></div>
  <h1 class="hero-title" style="font-weight:400">Are you looking for wedding vendors?</h1>
  <p class="hero-sub">Lorem ipsum dolor sit amet, consectetur apiscing elit, sed do eiusmod tempor incididunt ut labore et dolore magna aliqua.</p>
  <div class="search">
    <div class="search-field" style="width:158px;border-right:1px solid #ddd">Location <span>▾</span></div>
    <div class="search-field" style="width:267px;padding-left:46px;padding-right:70px">Wedding Venues <span>▾</span></div>
    <div class="search-btn">Get Started</div>
  </div>
</section>

<section>
  <div class="abs features"></div>
  <h2 class="section-title" style="top:796px;font-weight:400">Our Features</h2>
  <div class="feature" style="left:100px;top:876px"><div class="ic"><svg width="38" height="38" viewBox="0 0 38 38" fill="none" stroke="#6a2c7b" stroke-width="2"><rect x="4" y="7" width="30" height="26" rx="2"/><path d="M4 14h30M11 4v6M27 4v6M10 19h4M17 19h4M24 19h4M10 25h4M17 25h4M24 25h4"/></svg></div><p>User-friendly and intuitive booking process. Each vendor lists multiple packages for instant purchase</p></div>
  <div class="feature" style="left:354px;top:876px"><div class="ic"><svg width="38" height="38" viewBox="0 0 38 38" fill="none" stroke="#6a2c7b" stroke-width="2"><path d="M4 16L19 5l15 11v17H4z"/><path d="M14 33V22h10v11"/></svg></div><p>Detailed information about each vendor and venue, including pictures and descriptions</p></div>
  <div class="feature" style="left:608px;top:876px"><div class="ic"><svg width="38" height="38" viewBox="0 0 38 38" fill="none" stroke="#6a2c7b" stroke-width="2"><rect x="4" y="5" width="8" height="8"/><rect x="15" y="5" width="8" height="8"/><rect x="26" y="5" width="8" height="8"/><path d="M17 34V18a2 2 0 014 0v8l6 1v7"/></svg></div><p>Ability to view and select vendors and venues based on location, price, and other criteria</p></div>
  <div class="feature" style="left:863px;top:876px"><div class="ic"><svg width="38" height="38" viewBox="0 0 38 38" fill="none" stroke="#6a2c7b" stroke-width="2"><rect x="4" y="10" width="26" height="18" rx="2"/><path d="M4 15h26M8 23h8"/><rect x="10" y="16" width="24" height="16" rx="2"/></svg></div><p>Multiple online payment options, including credit card, bank transfers, &amp; Flexible payment</p></div>
  <div class="feature" style="left:100px;top:1082px"><div class="ic"><svg width="38" height="38" viewBox="0 0 38 38" fill="none" stroke="#6a2c7b" stroke-width="2"><path d="M19 4l12 5v9c0 8-5 13-12 16-7-3-12-8-12-16V9z"/><path d="M13 19l4 4 8-8"/></svg></div><p>All booking are automatically insuranced for, so that couples have peace of mind and</p></div>
  <div class="feature" style="left:354px;top:1082px"><div class="ic"><svg width="38" height="38" viewBox="0 0 38 38" fill="none" stroke="#6a2c7b" stroke-width="2"><circle cx="19" cy="13" r="7"/><path d="M6 34c2-8 7-11 13-11s11 3 13 11"/></svg></div><p>Personalized recommendations for vendors and venues based on couples' preferences &amp; wedding plans</p></div>
  <div class="feature" style="left:608px;top:1082px"><div class="ic"><svg width="38" height="38" viewBox="0 0 38 38" fill="none" stroke="#6a2c7b" stroke-width="2"><path d="M3 17l7-7 6 3 6-3 6 3 7 4-9 9-5-4M3 17l10 10 3-3"/></svg></div><p>Loyalty program or rewards system for couples who book multiple vendors or venues through</p></div>
  <div class="feature" style="left:863px;top:1082px"><div class="ic"><svg width="38" height="38" viewBox="0 0 38 38" fill="none" stroke="#6a2c7b" stroke-width="2"><rect x="7" y="6" width="24" height="28" rx="2"/><path d="M14 4h10v5H14zM12 16l2 2 3-3M20 17h7M12 25l2 2 3-3M20 26h7"/></svg></div><p>Access to resources and tools, such as wedding planning guides and checklists</p></div>
  <div class="btn" style="left:525px;top:1309px;width:151px;height:39px">VIEW MORE</div>
</section>

<section>
  <h2 class="section-title" style="top:1530px;font-weight:400">Find Your Dream Vendors</h2>
  <div class="vendor" style="left:100px;top:1600px;background:linear-gradient(160deg,#6b5a3a,#2a2420 60%,#b8a8a0)" role="img" aria-label="Photo of a lit wedding reception tent"><i></i><span>Wedding Venue</span></div>
  <div class="vendor" style="left:352px;top:1600px;background:linear-gradient(160deg,#c9b8a8,#e8d6c4 50%,#8b7565)" role="img" aria-label="Photo of makeup being applied"><i></i><span>Hair / Make Up</span></div>
  <div class="vendor" style="left:605px;top:1600px;background:linear-gradient(160deg,#b8cde0,#e6e0e4 55%,#d8a9b8)" role="img" aria-label="Photo of a photographer shooting a couple"><i></i><span>Photography / Videography</span></div>
  <div class="vendor" style="left:858px;top:1600px;background:linear-gradient(160deg,#d25a6a,#8a1f2a 55%,#3d2a2a)" role="img" aria-label="Photo of red roses"><i></i><span>Wedding Essentials</span></div>
  <div class="vendor" style="left:100px;top:1843px;background:linear-gradient(160deg,#7a1a3a,#1a2e70 55%,#0c1030)" role="img" aria-label="Photo of DJ headphones and mixer"><i></i><span>DJ / Entertainment</span></div>
  <div class="vendor" style="left:352px;top:1843px;background:linear-gradient(160deg,#3e5a2e,#b05a6a 55%,#4a3a2a)" role="img" aria-label="Photo of a floral wedding arch"><i></i><span>Decor / Florist</span></div>
  <div class="vendor" style="left:605px;top:1843px;background:linear-gradient(160deg,#f0ece6,#d8cfc6 55%,#9a8a7e)" role="img" aria-label="Photo of a decorated banquet table"><i></i><span>Wedding Planner</span></div>
  <div class="vendor" style="left:858px;top:1843px;background:linear-gradient(160deg,#5a6a4a,#c8b8a0 55%,#3a3a30)" role="img" aria-label="Photo of guests toasting with glasses"><i></i><span>Catering</span></div>
</section>

<section>
  <div class="abs how" role="img" aria-label="Purple-tinted photo of a wedding reception"></div>
  <h2 class="section-title" style="top:2240px;color:#fff;font-weight:400">How It Works?</h2>
  <div class="step" style="left:108px"><svg class="ring" width="208" height="208" viewBox="0 0 208 208" fill="none"><path d="M104 4a100 100 0 0 1 100 100a100 100 0 0 1-100 100" stroke="#b969ae" stroke-width="8"/></svg><svg class="ic" viewBox="0 0 60 60" fill="none" stroke="#444" stroke-width="2"><circle cx="30" cy="20" r="10"/><path d="M12 56c2-14 9-20 18-20s16 6 18 20M22 12h16"/></svg><p>Explore Vendors over 18+ Categories</p></div>
  <div class="step" style="left:370px"><svg class="ring" width="208" height="208" viewBox="0 0 208 208" fill="none"><path d="M104 4a100 100 0 0 1 100 100a100 100 0 0 1-100 100" stroke="#b969ae" stroke-width="8"/></svg><svg class="ic" viewBox="0 0 60 60" fill="none" stroke="#444" stroke-width="2"><rect x="12" y="8" width="30" height="42" rx="2"/><path d="M18 18h18M18 26h18M18 34h10M36 48l14-20 4 3-14 20-5 2z"/></svg><p>Send us your Desired Requirements</p></div>
  <div class="step" style="left:633px"><svg class="ring" width="208" height="208" viewBox="0 0 208 208" fill="none"><path d="M104 4a100 100 0 0 1 100 100a100 100 0 0 1-100 100" stroke="#b969ae" stroke-width="8"/></svg><svg class="ic" viewBox="0 0 60 60" fill="none" stroke="#444" stroke-width="2.5"><path d="M8 14h18v14c0 10-6 16-14 18M34 14h18v14c0 10-6 16-14 18"/></svg><p>Get a Free Quote and Compare</p></div>
  <div class="step" style="left:896px"><svg class="ring" width="208" height="208" viewBox="0 0 208 208" fill="none"><path d="M104 4a100 100 0 0 1 100 100a100 100 0 0 1-100 100" stroke="#b969ae" stroke-width="8"/></svg><svg class="ic" viewBox="0 0 60 60" fill="none" stroke="#444" stroke-width="2"><path d="M4 26l10-10 8 4 8-4 8 4 10 6-12 12-7-5M4 26l14 14 4-4"/></svg><p>Pick Best Deal and Book Vendors</p></div>
  <svg class="arrow" style="left:305px" width="22" height="16" viewBox="0 0 22 16" fill="none" stroke="#d3a5cf" stroke-width="2"><path d="M0 8h20M13 1l7 7-7 7"/></svg>
  <svg class="arrow" style="left:567px" width="22" height="16" viewBox="0 0 22 16" fill="none" stroke="#d3a5cf" stroke-width="2"><path d="M0 8h20M13 1l7 7-7 7"/></svg>
  <svg class="arrow" style="left:830px" width="22" height="16" viewBox="0 0 22 16" fill="none" stroke="#d3a5cf" stroke-width="2"><path d="M0 8h20M13 1l7 7-7 7"/></svg>
</section>

<section>
  <div class="abs about" role="img" aria-label="Photo of a bride and groom dancing in a reception hall"></div>
  <div class="about-box">
    <h2>About Us</h2>
    <p>At vero eos et accusamus et iusto odio dignissimos ducimus qui blanditiis praesentium voluptatum deleniti atque corrupti quos dolores et quas molestias excepturi sint occaecati cupiditate non provident, similique sunt in culpa qui officia deserunt mollitia animi, id est laborum et dolorum fuga. Et harum quidem</p>
    <div class="btn" style="left:24px;top:290px;width:152px;height:38px">LEARN MORE</div>
  </div>
</section>

<section>
  <div class="abs clients"></div>
  <h2 class="section-title" style="top:3200px;font-weight:400">Our Happy Clients</h2>
  <div class="underline" style="top:3270px"><b></b></div>
  <p class="quote">At vero eos et accusamus et iusto odio dignissimos ducimus qui blanditiis praesentium voluptatum deleniti atque corrupti quos dolores et quas molestias excepturi sint occaecati cupiditate non provident, similique sunt in culpa qui officia deserunt mollitia animi, id est laborum et dolorum fuga.</p>
  <div class="abs" style="left:0;top:3412px;width:1200px;text-align:center;font-size:16px;font-weight:500">Clara Wynn</div>
  <div class="abs" style="left:0;top:3438px;width:1200px;text-align:center;font-size:20px;color:var(--gold);letter-spacing:1px">★★★★★</div>
  <svg class="abs" style="left:555px;top:3480px" width="90" height="14" viewBox="0 0 90 14" fill="none" stroke="#6a2c7b" stroke-width="1.5"><circle cx="7" cy="7" r="5.5"/><circle cx="31" cy="7" r="5.5"/><circle cx="55" cy="7" r="5.5" fill="#6a2c7b"/><circle cx="79" cy="7" r="5.5"/></svg>
</section>

<section>
  <h2 class="section-title" style="top:3672px;font-weight:400">Latest Blog</h2>
  <div class="underline" style="top:3731px"><b></b></div>
  <article class="post" style="left:100px"><div class="img" style="background:linear-gradient(160deg,#5a3a2a,#c8b8a8 50%,#6a4a3a)" role="img" aria-label="Photo of a couple standing by tall windows"></div><h3>The standard Lorem Ipsum ge, used since the 1500s</h3><p>Lorem ipsum dolor sitmet, consectr adipiscing elit, sed do eiusmod tempor incididunt ut labore et dolore magna aliqua.</p><a>LEARN MORE</a></article>
  <article class="post" style="left:444px"><div class="img" style="background:linear-gradient(180deg,#5a7aa8,#c89a70 55%,#6a4a3a)" role="img" aria-label="Photo of an outdoor dinner under paper lanterns"></div><h3>The standard Lorem Ipsum ge, used since the 1500s</h3><p>Lorem ipsum dolor sitmet, consectr adipiscing elit, sed do eiusmod tempor incididunt ut labore et dolore magna aliqua.</p><a>LEARN MORE</a></article>
  <article class="post" style="left:787px"><div class="img" style="background:linear-gradient(160deg,#f0e6e0,#d8b8a8 55%,#a87868)" role="img" aria-label="Photo of hands with an engagement ring"></div><h3>The standard Lorem Ipsum ge, used since the 1500s</h3><p>Lorem ipsum dolor sitmet, consectr adipiscing elit, sed do eiusmod tempor incididunt ut labore et dolore magna aliqua.</p><a>LEARN MORE</a></article>
</section>

<footer>
  <div class="abs footer"></div>
  <div class="signup">
    <h4>Sign Up To Get<br>Exclusive Information</h4>
    <div class="inputs"><span style="padding-left:20px;width:168px;border-right:1px solid #ccc;line-height:34px">Full Name</span><span style="padding-left:44px">Email Address</span></div>
    <div class="submit">Submit</div>
  </div>
  <div class="fcol" style="left:100px"><h5>Quick Links</h5><ul><li>About</li><li>Contact Us</li><li>Our Wedding Blogs</li><li>Customer FAQs</li><li>Vendor FAQs</li></ul></div>
  <div class="fcol" style="left:359px"><h5>Other Links</h5><ul><li>Faq</li><li>Terms Of Service</li><li>Contact</li></ul></div>
  <div class="fcol" style="left:603px"><h5>Our Services</h5><ul><li>Wedding Photography</li><li>Bridal Makeup</li><li>Bridal Mehndi</li><li>Bridal Outfits</li><li>Rental Transportation</li></ul></div>
  <div class="fcol" style="left:882px"><h5>Planning &amp; Inspiration</h5><ul><li>Search Vendors</li><li>Destination Weddings</li><li>Submit your Wedding</li></ul></div>
  <span class="social" style="left:882px" aria-label="Social link"></span>
  <span class="social" style="left:926px" aria-label="Social link"></span>
  <span class="social" style="left:970px" aria-label="Social link"></span>
  <span class="social" style="left:1014px" aria-label="Social link"></span>
  <div class="fline"></div>
  <div class="copy">©Copyright ©2022 Brindlemoor. All Rights Reserved.</div>
</footer>

</div>
</body>
</html>
```